Billboard design 8x3M ONDALIX (Spanish company)

We´re located in the south of Spain. We run a local telecom company.
We sell Fiber optic, and mobile phone lines mainly.
The billboard will have to be in Spanish, I would like the price to be something you spot on first sight when passing by in the car.
Our company color is blue, like in our logo which I will add. I will also add a example from what we currently have.
The new offer should be:
1000 megas + 100Gigas movil con llamadas ilimitadas. (meaning 1000Mb fiber optic speed and 100Gb data and unlimited calls for 1 mobile line)
Our details are: phone line 000 00 0000
Website: ondalix.example

```html
<!DOCTYPE html>
<html lang="es">
<head>
<meta charset="utf-8">
<title>ONDALIX – Valla 8x3</title>
<link rel="stylesheet" href="https://fonts.googleapis.com/css2?family=Montserrat:wght@600;700;800;900&family=Rubik:wght@500;700;800&display=swap">
<style>
  :root {
    --navy-deep: #0a1f4a;
    --navy: #123a7a;
    --blue-bright: #2f7fe0;
    --cyan-glow: #52c6ff;
    --red: #e03a2c;
    --white: #ffffff;
    --page: #e9ebef;
  }
  * { box-sizing: border-box; margin: 0; padding: 0; }
  html, body {
    width: 1200px; height: 798px; overflow: hidden;
    background: var(--page);
  }
  .billboard {
    position: absolute; left: 0; top: 174px;
    width: 1200px; height: 450px; overflow: hidden;
    background:
      linear-gradient(90deg, rgba(10,31,74,0) 45%, rgba(82,198,255,0.22) 72%, rgba(10,31,74,0) 100%),
      linear-gradient(180deg, var(--navy) 0%, var(--navy-deep) 100%);
    color: var(--white);
  }
  .photo-area {
    position: absolute; left: 460px; top: 40px; width: 360px; height: 400px;
    background: linear-gradient(90deg,
      rgba(10,31,74,0) 0%,
      rgba(200,56,47,0.45) 22%,
      rgba(154,163,179,0.55) 48%,
      rgba(120,140,150,0.55) 72%,
      rgba(47,127,224,0) 100%);
  }
  .brand-block { position: absolute; left: 44px; top: 40px; width: 430px; font-family: "Montserrat", sans-serif; }
  .brand-name {
    display: flex; align-items: center; gap: 12px;
    font-size: 74px; font-weight: 900; line-height: 1; letter-spacing: 1px;
  }
  .brand-dot { width: 20px; height: 20px; border-radius: 50%; background: var(--white); }
  .brand-services { margin-top: 12px; font-size: 20px; font-weight: 700; }
  .headline { margin-top: 18px; font-size: 28px; font-weight: 800; line-height: 1.2; text-transform: uppercase; }
  .divider { margin-top: 20px; width: 400px; height: 14px; border-radius: 7px; background: var(--red); }
  .contact-phone {
    margin-top: 20px; display: flex; align-items: center; gap: 16px;
    color: var(--red); font-size: 40px; font-weight: 800; line-height: 1.1;
  }
  .contact-web { margin-top: 8px; color: var(--red); font-size: 32px; font-weight: 800; }
  .conditions {
    position: absolute; right: 44px; top: 22px;
    font-family: "Rubik", sans-serif; font-size: 14px; font-weight: 700;
  }
  .offer { position: absolute; right: 40px; top: 50px; width: 360px; font-family: "Rubik", sans-serif; text-align: right; }
  .speed-badge {
    display: inline-flex; align-items: baseline; gap: 8px;
    background: var(--red); border-radius: 24px; padding: 10px 24px 14px;
    font-weight: 800;
  }
  .speed-value { font-size: 86px; line-height: 1; letter-spacing: -2px; }
  .speed-unit { font-size: 40px; }
  .data-line { margin-top: 12px; font-size: 62px; font-weight: 700; line-height: 1; }
  .mobile-line {
    margin-top: 8px; display: flex; justify-content: flex-end; align-items: center; gap: 22px;
    font-size: 66px; font-weight: 700; line-height: 1;
  }
  .price-line { margin-top: 6px; display: flex; justify-content: flex-end; align-items: baseline; gap: 14px; font-weight: 800; }
  .price-prefix { font-size: 24px; }
  .price-value { font-size: 88px; line-height: 1; letter-spacing: -2px; }
</style>
</head>
<body>
  <section class="billboard">
    <div class="photo-area" role="img" aria-label="Foto de un joven con gorro rojo patinando en monopatín con estelas de velocidad"></div>

    <div class="brand-block">
      <div class="brand-name"><span>ONDALIX</span><span class="brand-dot"></span></div>
      <p class="brand-services">Wifi | Fibra | Movil | Tv</p>
      <h1 class="headline">Tu fibra + móvil<br>al mejor precio</h1>
      <div class="divider"></div>
      <p class="contact-phone">
        <svg width="24" height="40" viewBox="0 0 24 40" aria-hidden="true">
          <rect x="2" y="2" width="20" height="36" rx="4" fill="none" stroke="#ffffff" stroke-width="3"/>
          <circle cx="12" cy="32" r="2" fill="#ffffff"/>
        </svg>
        000 00 0000
      </p>
      <p class="contact-web">www.ondalix.example</p>
    </div>

    <p class="conditions">*Consulte condiciones</p>

    <div class="offer">
      <div class="speed-badge"><span class="speed-value">1000</span><span class="speed-unit">Mb</span></div>
      <p class="data-line">+ 100 Gb</p>
      <p class="mobile-line">
        <svg width="36" height="60" viewBox="0 0 40 66" aria-hidden="true">
          <rect x="3" y="3" width="34" height="60" rx="6" fill="none" stroke="#ffffff" stroke-width="5"/>
          <circle cx="20" cy="53" r="3" fill="#ffffff"/>
        </svg>
        <span>móvil</span>
      </p>
      <p class="price-line"><span class="price-prefix">por</span><span class="price-value">18.45€</span></p>
    </div>
  </section>
</body>
</html>
```